Design new modern Business Cards

I'm looking for a new modern business card & Stationery design.
We are an Architectural Lighting business that imports products from Europe and Australasia.
see our website for further information: [url removed, login to view]
- Card is to be double sided.
- Design is to be based on 4 colours: White, Green, Grey and Black ( Can provide Colour Number)
- successful design is to be supplied in Indesign format for future updates.

```html
<!DOCTYPE html>
<html lang="en">
<head>
<meta charset="utf-8">
<title>Lumevo Business Cards</title>
<link href="https://fonts.googleapis.com/css2?family=Arimo:wght@400;700&display=swap" rel="stylesheet">
<style>
  :root {
    --green: #8cb82b;
    --grey-dark: #3f3f41;
    --grey-text: #4a4a4c;
    --black: #1d1d1f;
    --white: #ffffff;
    --backdrop: #eceeef;
  }
  * { margin: 0; padding: 0; box-sizing: border-box; }
  html, body {
    width: 1200px; height: 900px; overflow: hidden;
    background: var(--backdrop);
    font-family: "Arimo", Arial, sans-serif;
  }
  .sheet { position: relative; width: 1200px; height: 900px; }
  .card {
    position: absolute; left: 300px;
    width: 600px; height: 343px;
    background: var(--white);
    box-shadow: 0 6px 18px rgba(0,0,0,0.12);
    overflow: hidden;
  }
  .card--front { top: 90px; }
  .card--back { top: 467px; }
  .card__shape { position: absolute; inset: 0; }

  .brand-name {
    position: absolute;
    font-family: "Arimo", Arial, sans-serif;
    font-weight: 700; font-size: 42px; line-height: 1;
    letter-spacing: 1px;
    color: var(--grey-dark);
  }
  .card--front .brand-name { left: 88px; top: 92px; }
  .card--back .brand-name { left: 0; right: 0; top: 140px; text-align: center; }

  .person {
    position: absolute; left: 88px; top: 178px; width: 210px;
    text-align: right; color: var(--grey-text);
  }
  .person__name { font-size: 15px; font-weight: 700; color: var(--green); }
  .person__creds { font-size: 11px; margin-top: 2px; }
  .person__role { font-size: 11.5px; font-weight: 700; color: var(--green); margin-top: 6px; }
  .person__address { font-size: 11px; line-height: 1.35; margin-top: 6px; }

  .divider {
    position: absolute; left: 312px; top: 172px;
    width: 1.5px; height: 104px; background: var(--green);
  }
  .contacts {
    position: absolute; left: 326px; top: 172px;
    list-style: none; color: var(--black); font-size: 11.5px;
  }
  .contacts li { display: flex; align-items: center; gap: 12px; height: 26px; }
  .contacts svg { width: 14px; height: 14px; fill: var(--green); flex: none; }

  .web {
    position: absolute; right: 140px; top: 206px;
    font-size: 11.5px; color: var(--grey-text);
  }
</style>
</head>
<body>
<main class="sheet">

  <section class="card card--front" aria-label="Business card front">
    <svg class="card__shape" viewBox="0 0 600 343" preserveAspectRatio="none" aria-hidden="true">
      <rect width="600" height="343" fill="var(--green)"/>
      <ellipse cx="300" cy="171" rx="345" ry="232" fill="var(--white)"/>
    </svg>

    <p class="brand-name">LUMEVO</p>

    <div class="person">
      <p class="person__name">DR. ELSA MARVIN</p>
      <p class="person__creds">BCMP (HONS.), ND</p>
      <p class="person__role">NATUROPATHIC DOCTOR</p>
      <p class="person__address">42 Harbourview Rd, Suite 210<br>Elmwood, ON N2K 4B7</p>
    </div>

    <div class="divider"></div>

    <ul class="contacts">
      <li>
        <svg viewBox="0 0 24 24" aria-hidden="true"><path d="M6.6 10.8a15 15 0 0 0 6.6 6.6l2.2-2.2a1 1 0 0 1 1-.25 11.4 11.4 0 0 0 3.6.57 1 1 0 0 1 1 1V20a1 1 0 0 1-1 1A17 17 0 0 1 3 4a1 1 0 0 1 1-1h3.5a1 1 0 0 1 1 1c0 1.25.2 2.45.57 3.6a1 1 0 0 1-.25 1z"/></svg>
        555-014-2281
      </li>
      <li>
        <svg viewBox="0 0 24 24" aria-hidden="true"><path d="M6 3h10l2 2v4H6zM3 10h18v8h-3v3H6v-3H3zm5 6v3h8v-3z"/></svg>
        555-014-2282
      </li>
      <li>
        <svg viewBox="0 0 24 24" aria-hidden="true"><path d="M2 5h20v14H2zm2 2v.5l8 5.5 8-5.5V7zm0 3v7h16v-7l-8 5.5z"/></svg>
        info@NorthfieldWellness.com
      </li>
      <li>
        <svg viewBox="0 0 24 24" aria-hidden="true"><circle cx="12" cy="12" r="9" fill="none" stroke="var(--green)" stroke-width="2"/><path d="M3 12h18M12 3c3 3 3 15 0 18M12 3c-3 3-3 15 0 18" fill="none" stroke="var(--green)" stroke-width="1.6"/></svg>
        www.NorthfieldWellness.com
      </li>
    </ul>
  </section>

  <section class="card card--back" aria-label="Business card back">
    <svg class="card__shape" viewBox="0 0 600 343" preserveAspectRatio="none" aria-hidden="true">
      <rect width="600" height="343" fill="var(--green)"/>
      <ellipse cx="300" cy="171" rx="345" ry="232" fill="var(--white)"/>
    </svg>

    <p class="brand-name">LUMEVO</p>

    <p class="web">www.lumevolighting.com.au</p>
  </section>

</main>
</body>
</html>
```